Adelaide based cleaning and remediation business needs a website design

We are launching a new company with no clients as yet so we don't have the benefit of Trelvox Ratings to build confidence. We can use our  past work history with other employers in the industry to give some credibility. Happy to use any colour scheme as long as it look interesting when people click on the site it gets there attention. enquiry . I have supplied a mock up the important information and various photos as they tell a lot of the story.

```html
<!DOCTYPE html>
<html lang="en">
<head>
<meta charset="utf-8">
<title>Marlow Services – Dirty Job Cleaners</title>
<link href="https://fonts.googleapis.com/css2?family=Figtree:wght@400;500;600;700&display=swap" rel="stylesheet">
<style>
:root{
  --navy:#0d4460;
  --ink:#113a52;
  --blue:#0b72b6;
  --yellow:#f6b51a;
  --teal:#3b6a7b;
  --lavender:#f3f4fb;
  --muted:#5a6b78;
  --white:#ffffff;
  --line:#b9c3cc;
}
*{box-sizing:border-box;margin:0;padding:0}
html,body{width:1200px;height:4415px;overflow:hidden}
body{position:relative;background:var(--white);font-family:"Figtree",sans-serif;color:var(--ink)}
.abs{position:absolute}
.btn{position:absolute;display:flex;align-items:center;justify-content:center;background:var(--blue);color:var(--white);border-radius:20px;font-size:10px;font-weight:600}
.btn-outline{position:absolute;display:flex;align-items:center;justify-content:center;border:1.5px solid var(--blue);color:var(--blue);border-radius:20px;font-size:9px;font-weight:600;background:var(--white)}
.eyebrow{position:absolute;left:0;width:1200px;text-align:center;font-size:10px;font-weight:600;color:var(--yellow)}
.section-title{position:absolute;left:0;width:1200px;text-align:center;font-size:31px;font-weight:500;line-height:38px;color:var(--ink)}

/* header */
.site-header{position:absolute;left:0;top:0;width:1200px;height:62px;background:var(--white);z-index:5}
.brand-badge{position:absolute;left:107px;top:-18px;width:86px;height:86px;border-radius:50%;background:var(--white);box-shadow:0 2px 6px rgba(0,0,0,.15);z-index:6;display:flex;align-items:center;justify-content:center;padding-top:16px;font-size:15px;font-weight:700;color:var(--navy)}
.brand-name{position:absolute;left:209px;top:21px;font-size:14px;font-weight:500;color:var(--navy)}
.main-nav{position:absolute;left:456px;top:24px;display:flex;font-size:11px;font-weight:500;color:var(--navy)}
.main-nav span{margin-right:25px}
.main-nav .active{color:var(--blue)}

/* hero */
.hero{position:absolute;left:0;top:62px;width:1200px;height:560px}
.hero-kicker{position:absolute;left:0;top:160px;width:1200px;text-align:center;color:var(--white);font-size:15px;font-weight:500}
.hero-title{position:absolute;left:0;top:192px;width:1200px;text-align:center;color:var(--white);font-size:62px;line-height:74px;font-weight:600;letter-spacing:-.5px}

/* about */
.about-label{position:absolute;left:200px;top:700px;font-size:10px;font-weight:600;color:var(--blue)}
.about-title{position:absolute;left:200px;top:724px;width:400px;font-size:31px;line-height:38px;font-weight:500;color:var(--ink)}
.about-text{position:absolute;left:200px;width:400px;font-size:12px;line-height:19px;color:var(--muted)}
.about-photo{position:absolute;border-radius:50%}

/* services */
.services-bg{position:absolute;left:0;top:1488px;width:1200px;height:1560px;background:var(--lavender)}
.service-card{position:absolute;top:1382px;width:312px;height:312px;background:var(--white)}
.service-card .photo{height:157px;width:100%}
.service-card h3{position:absolute;left:18px;top:178px;font-size:16px;font-weight:600;color:var(--navy)}
.service-card p{position:absolute;left:18px;top:208px;width:280px;font-size:10px;line-height:15.5px;color:var(--muted)}
.service-card .btn-outline{left:16px;top:270px;width:90px;height:22px}
.insured{position:absolute;left:0;top:1746px;width:1200px;text-align:center;color:var(--white);font-size:18px;line-height:27px;font-weight:500}

/* gallery */
.gallery-photo{position:absolute}

/* testimonials */
.review-card{position:absolute;top:3219px;width:250px;height:192px;background:var(--white);box-shadow:0 3px 6px rgba(0,0,0,.25)}
.review-card .quote-mark{position:absolute;left:12px;top:14px;width:30px;height:30px;border-radius:50%;background:#f4f1e8;color:var(--yellow);font-size:22px;font-weight:700;text-align:center;line-height:34px}
.review-card .name{position:absolute;left:52px;top:16px;font-size:11px;font-weight:600;color:var(--navy)}
.review-card .role{position:absolute;left:52px;top:34px;font-size:9px;color:var(--muted)}
.review-card .stars{position:absolute;left:14px;top:56px;font-size:15px;letter-spacing:2px;color:var(--yellow)}
.review-card p{position:absolute;left:14px;top:84px;width:225px;font-size:9px;line-height:15px;color:var(--muted)}
.review-card p b{color:var(--navy)}
.slider-arrow{position:absolute;top:3297px;width:32px;height:32px;border-radius:50%;border:1.5px solid var(--yellow)}

/* contact */
.field{position:absolute;height:37px;border:1px solid var(--line);border-radius:3px;background:var(--white);font-size:10px;color:var(--muted);padding:11px 12px}
.field.message{height:68px}

/* footer */
.footer-heading{position:absolute;top:4165px;font-size:12px;font-weight:600;color:var(--white)}
.footer-text{position:absolute;font-size:10px;line-height:19px;color:#d6e1e8}
.footer-links{position:absolute;left:656px;top:4190px;font-size:10px;line-height:19px;color:#d6e1e8}
.footer-links .active{color:var(--yellow)}
.contact-line{position:absolute;left:430px;display:flex;align-items:flex-start;gap:6px;font-size:10.5px;line-height:15px;color:#d6e1e8}
.social{position:absolute;top:4263px;width:30px;height:30px;border-radius:50%;border:1.5px solid var(--white)}
.legal{position:absolute;top:4379px;font-size:9px;color:#d6e1e8}
.legal .hl{color:var(--yellow)}
.card-chip{position:absolute;top:4375px;width:27px;height:17px;border-radius:3px;background:var(--white)}
</style>
</head>
<body>

<!-- header -->
<header class="site-header">
  <div class="brand-name">Marlow Services</div>
  <nav class="main-nav">
    <span class="active">Home</span><span>About us</span><span>Services</span><span>Pricing</span><span>Testimonials</span><span>Gallery</span><span>Contact us</span>
  </nav>
  <div class="btn" style="left:941px;top:15px;width:152px;height:31px">Schedule Your Cleaning</div>
</header>
<div class="brand-badge">Marlow</div>

<!-- hero -->
<section class="hero">
  <svg width="1200" height="560" viewBox="0 0 1200 560" class="abs" style="left:0;top:0">
    <defs>
      <linearGradient id="heroShade" x1="0" y1="0" x2="1" y2="1">
        <stop offset="0" stop-color="#6b5746"/>
        <stop offset=".5" stop-color="#4a3d33"/>
        <stop offset="1" stop-color="#7d7468"/>
      </linearGradient>
    </defs>
    <rect width="1200" height="560" fill="url(#heroShade)" role="img" aria-label="Photo of a cluttered, graffiti-marked room full of debris"/>
    <rect width="1200" height="560" fill="rgba(0,0,0,.25)"/>
    <path d="M0,375 Q600,615 1200,375 L1200,560 L0,560 Z" fill="#ffffff"/>
    <path d="M140,428 Q600,690 1060,428 Q600,650 140,428 Z" fill="#0d72b3"/>
    <path d="M150,432 Q600,672 1050,432" fill="none" stroke="#0d4460" stroke-width="1.5"/>
    <circle cx="600" cy="459" r="13" fill="none" stroke="rgba(255,255,255,.8)" stroke-width="1.2"/>
    <path d="M600,452 L600,465 M595,460 L600,465 L605,460" fill="none" stroke="rgba(255,255,255,.8)" stroke-width="1.2"/>
  </svg>
  <div class="hero-kicker">Marlow Services Pty Ltd</div>
  <h1 class="hero-title">Dirty Job Cleaners</h1>
  <div class="btn" style="left:550px;top:288px;width:98px;height:27px">Get a Quote</div>
</section>

<!-- about -->
<section>
  <div class="about-label">About us</div>
  <h2 class="about-title">Adelaide-based Marlow Services is a family-run organisation.</h2>
  <p class="about-text" style="top:866px">We have been in operation for more than two decades. We've gained some knowledge about cleaning and squalor removal services throughout the years.</p>
  <p class="about-text" style="top:940px">As a small South Australian company, we base everything on responsibility honesty and fairness. We are aware of the confidence you put in us when you seek our help.</p>
  <div class="btn" style="left:200px;top:1020px;width:109px;height:30px">Discover More</div>
  <div class="about-photo" style="left:643px;top:662px;width:356px;height:356px;background:linear-gradient(135deg,#5b4b3c,#7a6a55 55%,#4d6b3a)" role="img" aria-label="Photo of a yard piled with rusted scrap and a bicycle"></div>
  <div class="about-photo" style="left:698px;top:921px;width:164px;height:164px;border:5px solid #fff;background:linear-gradient(160deg,#4a5a66,#2f6aa6 50%,#4a3d30)" role="img" aria-label="Photo of a worker in protective suit sorting waste"></div>
</section>

<!-- services -->
<div class="services-bg"></div>
<svg width="1200" height="800" viewBox="0 1140 1200 800" class="abs" style="left:0;top:1140px">
  <polygon points="43,1166 43,1192 640,1176" fill="#f6b51a"/>
  <polygon points="43,1191 1167,1162 1167,1906 43,1934" fill="#0d4460"/>
  <polygon points="560,1921 1167,1905 1167,1934" fill="#f6b51a"/>
</svg>
<section>
  <div class="eyebrow" style="top:1240px">Our Signature&nbsp; Services</div>
  <h2 class="section-title" style="top:1263px;color:var(--white)">We do the stuff nobody<br>wants to do</h2>

  <article class="service-card" style="left:106px">
    <div class="photo" style="background:linear-gradient(180deg,#e9e6e0,#c8c2b6)" role="img" aria-label="Photo of pigeons perched on a stained building ledge"></div>
    <h3>Pigeon Waste</h3>
    <p>Can cause damage to buildings and&nbsp; spread disease, mites and bacteria, triggering alarms and damaging the reputation of businesses...</p>
    <div class="btn-outline">Read More</div>
  </article>
  <article class="service-card" style="left:444px">
    <div class="photo" style="background:linear-gradient(180deg,#4a3f36,#2a2420)" role="img" aria-label="Photo of a fire-damaged kitchen interior"></div>
    <h3>Fire Damage Clean Outs</h3>
    <p>Removal of debris; On site cleaning of contents; Cleaning of carpets and upholstered items; Catalogue all contents for packing and storage...</p>
    <div class="btn-outline">Read More</div>
  </article>
  <article class="service-card" style="left:782px">
    <div class="photo" style="background:linear-gradient(180deg,#6b5a48,#8d7a64)" role="img" aria-label="Photo of a hoarded room with packed shelves"></div>
    <h3>Squlaor Estate Clean ups</h3>
    <p>Marlow Services&nbsp; is a hoarding clean up firm that approaches clutter removal personally. We always operate with compassion&nbsp; prioritising...</p>
    <div class="btn-outline">Read More</div>
  </article>

  <p class="insured">We are fully insured for 20 million public liability and our team have current police and<br>working with vulnerable people clearances</p>
  <div class="btn" style="left:523px;top:1830px;width:154px;height:29px">Schedule Your Cleaning</div>
</section>

<!-- testimonials band -->
<svg width="1200" height="560" viewBox="0 3000 1200 560" class="abs" style="left:0;top:3000px">
  <polygon points="0,3016 0,3048 720,3030" fill="#f6b51a"/>
  <polygon points="0,3048 1200,3017 1200,3522 0,3548" fill="#3b6a7b"/>
  <polygon points="520,3535 1200,3522 1200,3550" fill="#f6b51a"/>
</svg>

<!-- gallery -->
<section>
  <div class="eyebrow" style="top:2012px">Photo Gallery</div>
  <h2 class="section-title" style="top:2036px">Cleaning and squalor<br>removal services</h2>
  <div class="gallery-photo" style="left:200px;top:2160px;width:436px;height:437px;background:linear-gradient(160deg,#8a8c88,#5e5a52 60%,#a7a39a)" role="img" aria-label="Photo of a shed filled with scattered rubbish and shelving"></div>
  <div class="gallery-photo" style="left:650px;top:2160px;width:349px;height:351px;background:linear-gradient(160deg,#6f7064,#4d5040 60%,#7a7a6a)" role="img" aria-label="Photo of heaped scrap metal and boxes in a shed"></div>
  <div class="gallery-photo" style="left:650px;top:2523px;width:349px;height:350px;background:linear-gradient(160deg,#2c2e30,#8a8c8e 50%,#3a3832)" role="img" aria-label="Photo of a worker in protective suit cleaning a roof cavity"></div>
  <div class="gallery-photo" style="left:200px;top:2611px;width:436px;height:437px;background:linear-gradient(160deg,#7d8a8c,#6a5442 55%,#5a6b3a)" role="img" aria-label="Photo of a yard with rusted scrap and a bicycle"></div>
  <div class="btn" style="left:785px;top:2924px;width:81px;height:29px">View All</div>
</section>

<!-- testimonials -->
<section>
  <div class="eyebrow" style="top:3124px">Testimonials</div>
  <h2 class="section-title" style="top:3150px;color:var(--white)">Happy clients say</h2>

  <div class="slider-arrow" style="left:143px" role="img" aria-label="Previous"><svg width="29" height="29" viewBox="0 0 29 29"><path d="M18,14.5 H11 M14,11.5 L11,14.5 L14,17.5" fill="none" stroke="#f6b51a" stroke-width="1.3"/></svg></div>
  <div class="slider-arrow" style="left:1024px" role="img" aria-label="Next"><svg width="29" height="29" viewBox="0 0 29 29"><path d="M11,14.5 H18 M15,11.5 L18,14.5 L15,17.5" fill="none" stroke="#f6b51a" stroke-width="1.3"/></svg></div>

  <article class="review-card" style="left:200px">
    <div class="quote-mark">“</div>
    <div class="name">Helena Varcoe</div>
    <div class="role">Pigeon Waste Clean</div>
    <div class="stars">★★★★★</div>
    <p>Nathan and his team arrived the next morning to clean up a rental property my husband and I own which and had been trashed&nbsp; by the tenants.&nbsp; he was the only contractor to return my call. they did an amazing job.. <b>[more]</b></p>
  </article>
  <article class="review-card" style="left:475px">
    <div class="quote-mark">“</div>
    <div class="name">Dana Pruett</div>
    <div class="role">Squlaor Estate Clean</div>
    <div class="stars">★★★★★</div>
    <p>Excellent service. very happy with outcome did the job as quoted.</p>
  </article>
  <article class="review-card" style="left:749px">
    <div class="quote-mark">“</div>
    <div class="name">Owen Tarrant</div>
    <div class="role">Norvale Building Maintenance</div>
    <div class="stars">★★★★★</div>
    <p>Engaged marlow services to clean bird poo from our commercial building facade . job was so well done it exceeded our expectations.</p>
  </article>

  <div class="btn" style="left:542px;top:3445px;width:114px;height:28px">View All Review</div>
</section>

<!-- contact -->
<section>
  <div class="eyebrow" style="top:3626px">Get a Quick Quote</div>
  <h2 class="section-title" style="top:3652px">Get in touch today</h2>
  <div class="field" style="left:312px;top:3723px;width:281px">Name</div>
  <div class="field" style="left:605px;top:3723px;width:281px">Phone</div>
  <div class="field" style="left:312px;top:3773px;width:281px">Email</div>
  <div class="field" style="left:605px;top:3773px;width:281px">Select Services
    <svg width="8" height="6" viewBox="0 0 8 6" class="abs" style="right:12px;top:16px"><path d="M1,1 L4,4 L7,1" fill="none" stroke="#5a6b78" stroke-width="1"/></svg>
  </div>
  <div class="field message" style="left:312px;top:3821px;width:574px">Message</div>
  <div class="btn" style="left:562px;top:3905px;width:76px;height:29px">Submit</div>
</section>

<!-- footer -->
<svg width="1200" height="520" viewBox="0 3895 1200 520" class="abs" style="left:0;top:3895px">
  <path d="M0,4140 Q600,3934 1200,4140 L1200,4415 L0,4415 Z" fill="#0d4460"/>
  <path d="M125,4132 Q600,3870 1075,4132 Q600,3925 125,4132 Z" fill="#f6b51a"/>
</svg>
<footer>
  <div class="abs" style="left:200px;top:4160px;font-size:19px;font-weight:600;color:var(--white)">Marlow services</div>
  <p class="footer-text" style="left:200px;top:4195px;width:180px">Adelaide-based Marlow Services is a family-run organisation. We have been in operation for more than two decades.</p>

  <div class="footer-heading" style="left:430px">Contact us</div>
  <div class="contact-line" style="top:4198px;font-size:12px">
    <svg width="11" height="11" viewBox="0 0 12 12"><path d="M2,1 L4.5,1 L5.5,3.5 L4,4.8 Q5.2,7 7.2,8 L8.5,6.5 L11,7.5 L11,10 Q6,11 2,6 Q1,3.5 2,1 Z" fill="#f6b51a"/></svg>0412 555 019</div>
  <div class="contact-line" style="top:4223px">
    <svg width="11" height="9" viewBox="0 0 11 9"><rect x="0.5" y="0.5" width="10" height="8" rx="1" fill="#f6b51a"/><path d="M1,1 L5.5,5 L10,1" fill="none" stroke="#0d4460" stroke-width="1"/></svg>admin@marlowservices.com</div>
  <div class="contact-line" style="top:4248px">
    <svg width="10" height="13" viewBox="0 0 10 13"><path d="M5,12.5 Q0.5,7 0.5,4.8 A4.5,4.5 0 0 1 9.5,4.8 Q9.5,7 5,12.5 Z" fill="#f6b51a"/><circle cx="5" cy="4.8" r="1.6" fill="#0d4460"/></svg>27 Orrin Lane Kensal Park<br>SA 5099</div>
  <div class="abs" style="left:430px;top:4296px;font-size:10px;color:var(--yellow)">Get Directions ↗</div>

  <div class="footer-heading" style="left:656px">Quick links</div>
  <div class="footer-links">
    <div class="active">Home</div><div>About us</div><div>Services</div><div>Pricing</div><div>Testimonials</div><div>Gallery</div><div>Contact us</div>
  </div>

  <div class="footer-heading" style="left:794px">Business hours</div>
  <div class="abs" style="left:794px;top:4192px;font-size:10px;color:#d6e1e8"><b style="color:var(--white);font-weight:600">Monday to Saturday:</b> 8:00 AM - 4:00 PM</div>
  <div class="abs" style="left:794px;top:4232px;font-size:12px;font-weight:600;color:var(--white)">Follow us</div>
  <div class="social" style="left:794px" role="img" aria-label="Social profile 1"></div>
  <div class="social" style="left:832px" role="img" aria-label="Social profile 2"></div>
  <div class="social" style="left:870px" role="img" aria-label="Social profile 3"></div>
  <div class="social" style="left:908px" role="img" aria-label="Social profile 4"></div>

  <svg width="18" height="20" viewBox="0 0 18 20" class="abs" style="left:1084px;top:4350px" role="img" aria-label="Back to top"><path d="M9,1 L17,19 L9,14 L1,19 Z" fill="#f6b51a"/></svg>

  <div class="abs" style="left:200px;top:4360px;width:800px;height:1px;background:rgba(255,255,255,.2)"></div>
  <div class="legal" style="left:200px">© 2025 <span class="hl">Marlow Services.</span> All Rights Reserved</div>
  <div class="legal" style="left:424px">Privacy Policy&nbsp;&nbsp; |&nbsp;&nbsp; Terms and Conditions</div>
  <div class="legal" style="left:794px;color:var(--white);font-weight:600">We accept:</div>
  <div class="card-chip" style="left:855px" role="img" aria-label="Payment card"></div>
  <div class="card-chip" style="left:886px" role="img" aria-label="Payment card"></div>
  <div class="card-chip" style="left:917px" role="img" aria-label="Payment card"></div>
  <div class="card-chip" style="left:948px" role="img" aria-label="Payment card"></div>
  <div class="card-chip" style="left:979px" role="img" aria-label="Payment card"></div>
</footer>

</body>
</html>
```